Website for an AdOps/Media Agency

We need a logo for an ad operations firm. We help websites to maximize their advertising revenues by optimizing their ad networks, configurations, technologies, etc. The name is Zornival, or ZorNival, to communicate that we take them to the top of their revenue potential. We want to also communicate, trust us to handle your adops, we take care of the hassle (it's an industry in continual technological innovation -- hard to stay on top of, and heavily manual, reporting, etc) and make sure our clients maximize ad revenues. For more info on site ideas/desires: https://files.brelmora.com/doc/7QxTbn2Lw9Rk4Vz8Hc3Md6Fp1Ys5Ga0Je/view?usp=sharing
Updates

Project Deadline Extended Reason: Apologies, I got caught up in other things. This is now priority, and will be guaranteed. I will also include an extra coding fee for a WP site and increase the budget. Thanks for your understanding! Added Thursday, July 7, 2016

Target Market(s)

Ad Operations/Media Consultancy

Industry/Entity Type

Ad Agency

Number of Pages Required

1 page

Font styles to use
Sans Serif

Requirements
Must have
• I like clean and simple, nice images, scrolling down.
Nice to have
• I like clean, fresh white running through the site. Note, I listed us as an ad agency, but only because there was no adops. We work with ad agencies, but we are more agents for publishers.
Should not have
• To much clutter.

```html
<!DOCTYPE html>
<html lang="en">
<head>
<meta charset="utf-8">
<title>Zornival — Ad Operations</title>
<link href="https://fonts.googleapis.com/css2?family=Open+Sans:wght@300;400;600;700&display=swap" rel="stylesheet">
<style>
:root{
  --green:#4caf3e;
  --green-dark:#3d9632;
  --ink:#333333;
  --muted:#8a8a8a;
  --line:#e3e3e3;
  --dark:#2c2c2c;
  --darker:#1e1e1e;
  --white:#ffffff;
  --soft:#f6f6f6;
}
*{box-sizing:border-box;margin:0;padding:0}
html,body{width:1200px;height:2316px;overflow:hidden}
body{font-family:"Open Sans",Arial,sans-serif;color:var(--ink);background:var(--white);position:relative}
section,header,footer{position:absolute;left:0;width:1200px}

/* header */
.site-header{top:0;height:56px;background:var(--white);border-bottom:1px solid var(--line)}
.brand{position:absolute;left:120px;top:15px}
.brand-name{font-size:21px;font-weight:600;color:var(--ink);letter-spacing:.3px;line-height:26px}
.main-nav{position:absolute;right:120px;top:18px;display:flex;align-items:center;gap:22px;font-size:10px;font-weight:600;color:var(--muted);letter-spacing:.6px}
.main-nav .active{color:var(--green);border-bottom:2px solid var(--green);padding-bottom:3px}
.btn{display:inline-block;background:var(--green);color:var(--white);font-weight:600;border-radius:2px}
.main-nav .btn{padding:5px 14px;font-size:10px;letter-spacing:.4px}

/* hero */
.hero{top:56px;height:352px;overflow:hidden}
.hero-photo{position:absolute;inset:0;background:linear-gradient(135deg,#6f7478 0%,#a9acae 35%,#c9c6c0 55%,#8b8e90 80%,#5e6265 100%)}
.hero-shade{position:absolute;inset:0;background:rgba(30,34,38,.35)}
.hero-copy{position:absolute;left:0;right:0;top:182px;text-align:center;color:var(--white)}
.hero-title{font-size:30px;font-weight:400;line-height:34px}
.hero-sub{margin-top:8px;font-size:12px;line-height:15px;opacity:.9}
.hero .btn{margin-top:10px;padding:7px 18px;font-size:11px}
.hero-dots{position:absolute;top:336px;left:0;right:0;display:flex;justify-content:center;gap:6px}
.hero-dots span{width:7px;height:7px;border-radius:50%;background:rgba(255,255,255,.5)}
.hero-dots span.on{background:var(--white)}

/* section titles */
.section-title{text-align:center;font-size:30px;font-weight:400;color:var(--ink)}
.section-title em{font-style:normal;color:var(--green)}
.title-rule{display:block;width:40px;height:2px;background:var(--green);margin:10px auto 0}

/* services */
.services{top:530px;height:670px}
.service-grid{position:absolute;top:100px;left:160px;width:880px;display:grid;grid-template-columns:repeat(4,220px);grid-auto-rows:180px}
.service{text-align:center;padding:22px 18px 0}
.service-icon{width:56px;height:56px;margin:0 auto 12px;display:block}
.service-name{font-size:12px;font-weight:600;line-height:16px;color:var(--ink)}
.service.featured{background:#eef6ec;border:1px solid #d3e9cf;text-align:left;padding:16px 18px 0}
.service.featured .service-icon{margin:0 0 8px}
.service.featured .service-name{color:var(--green)}
.service-desc{margin-top:6px;font-size:10px;line-height:14px;color:var(--muted)}

/* welcome */
.welcome{top:1200px;height:288px;background:var(--dark);text-align:center;color:var(--white)}
.welcome .section-title{color:var(--white);padding-top:42px}
.welcome-text{width:900px;margin:26px auto 0;font-size:11px;line-height:18px;color:#b8b8b8}
.welcome .btn{margin-top:22px;padding:8px 20px;font-size:11px}

/* tools */
.tools{top:1488px;height:360px}
.tools .section-title{padding-top:42px}
.tool-list{position:absolute;top:120px;left:160px;width:880px;display:flex;gap:40px}
.tool{flex:1;height:152px;border:1px solid var(--line);display:flex;background:var(--white)}
.tool-icon{width:120px;background:var(--green);display:flex;align-items:center;justify-content:center}
.tool-body{padding:30px 24px}
.tool-name{font-size:20px;font-weight:400;line-height:24px;color:var(--ink)}
.tool-desc{margin-top:10px;font-size:10px;line-height:14px;color:var(--muted)}

/* partners */
.partners{top:1848px;height:152px;background:var(--white)}
.partner-row{position:absolute;top:8px;left:160px;width:880px;display:flex;justify-content:space-between}
.partner-badge{width:250px;height:104px;border:1px solid var(--line);display:flex;align-items:center;justify-content:center;background:var(--white)}
.partner-badge .mark{width:170px;height:46px;background:var(--soft);border-radius:4px}

/* contact */
.contact{top:2000px;height:276px;background:linear-gradient(180deg,#3a3d40 0%,#2a2c2e 100%);text-align:center;color:var(--white)}
.contact-title{padding-top:36px;font-size:30px;font-weight:300}
.contact-sub{margin-top:6px;font-size:11px;color:#b4b4b4}
.contact-form{position:absolute;top:130px;left:160px;width:880px}
.field-row{display:flex;gap:20px}
.field{flex:1;height:34px;background:var(--white);border:1px solid #d0d0d0;text-align:left;padding:9px 12px;font-size:11px;color:var(--muted)}
.contact-form .btn{margin-top:14px;padding:9px 28px;font-size:11px}

/* footer */
.site-footer{top:2276px;height:40px;background:var(--darker);color:#9a9a9a;font-size:10px}
.site-footer .copy{position:absolute;left:160px;top:13px}
.site-footer .mail{position:absolute;right:160px;top:13px}
</style>
</head>
<body>

<header class="site-header">
  <div class="brand"><span class="brand-name">Zornival</span></div>
  <nav class="main-nav">
    <span class="active">HOME</span><span>ABOUT US</span><span>SERVICES</span><span>TECHNOLOGY</span><span>PUBLISHERS</span><span>ADVERTISERS</span>
    <span class="btn">Sign Up</span>
  </nav>
</header>

<section class="hero">
  <div class="hero-photo" role="img" aria-label="Overhead photo of a team working together on laptops at a table"></div>
  <div class="hero-shade"></div>
  <div class="hero-copy">
    <h1 class="hero-title">One-stop shop for all<br>your monetization needs</h1>
    <p class="hero-sub">Let Our Team Do The Heavy Lifting To Optimize Your<br>Ad Revenue And Maximize Your Monetization.</p>
    <span class="btn">Free Consultation</span>
  </div>
  <div class="hero-dots"><span class="on"></span><span></span><span></span></div>
</section>

<section class="services">
  <h2 class="section-title"><em>Our</em> Services<span class="title-rule"></span></h2>
  <div class="service-grid">
    <div class="service featured">
      <svg class="service-icon" viewBox="0 0 56 56" fill="none" stroke="#4caf3e" stroke-width="3"><path d="M8 44 L22 30 L32 38 L48 16"/><path d="M38 16 H48 V26"/></svg>
      <div class="service-name">Monetization<br>Strategy &amp; Planning</div>
      <p class="service-desc">A tailored plan for every site, built around your audience, your inventory and your revenue goals.</p>
    </div>
    <div class="service">
      <svg class="service-icon" viewBox="0 0 56 56" fill="none" stroke="#333" stroke-width="3"><rect x="8" y="14" width="40" height="28"/><path d="M8 22 H48"/><rect x="14" y="28" width="10" height="8"/></svg>
      <div class="service-name">Access To Premium<br>Premier Exchange Account</div>
    </div>
    <div class="service">
      <svg class="service-icon" viewBox="0 0 56 56" fill="none" stroke="#333" stroke-width="3"><rect x="10" y="8" width="36" height="12"/><rect x="10" y="22" width="36" height="12"/><rect x="10" y="36" width="36" height="12"/><circle cx="16" cy="14" r="1.5"/><circle cx="16" cy="28" r="1.5"/><circle cx="16" cy="42" r="1.5"/></svg>
      <div class="service-name">Ad Server<br>Set up</div>
    </div>
    <div class="service">
      <svg class="service-icon" viewBox="0 0 56 56" fill="none" stroke="#333" stroke-width="3"><circle cx="28" cy="12" r="6"/><circle cx="12" cy="42" r="6"/><circle cx="44" cy="42" r="6"/><path d="M25 17 L15 37 M31 17 L41 37 M18 42 H38"/></svg>
      <div class="service-name">Network<br>Configurations</div>
    </div>

    <div class="service">
      <svg class="service-icon" viewBox="0 0 56 56" fill="none" stroke="#333" stroke-width="3"><circle cx="28" cy="28" r="9"/><path d="M28 8 V14 M28 42 V48 M8 28 H14 M42 28 H48 M14 14 L18 18 M38 38 L42 42 M42 14 L38 18 M14 42 L18 38"/></svg>
      <div class="service-name">Proprietary Performance<br>&amp; Reporting Tools</div>
    </div>
    <div class="service">
      <svg class="service-icon" viewBox="0 0 56 56" fill="none" stroke="#333" stroke-width="3"><path d="M14 20 L28 10 L36 20 L22 30 Z"/><path d="M25 26 L44 46"/><path d="M8 48 H30"/></svg>
      <div class="service-name">Header Bidder<br>Configuration</div>
    </div>
    <div class="service">
      <svg class="service-icon" viewBox="0 0 56 56" fill="none" stroke="#333" stroke-width="3"><path d="M10 10 H30 L46 26 L28 44 L10 26 Z"/><circle cx="20" cy="20" r="3"/></svg>
      <div class="service-name">Ad Tag<br>Implementation &amp; Tracking</div>
    </div>
    <div class="service">
      <svg class="service-icon" viewBox="0 0 56 56" fill="none" stroke="#333" stroke-width="3"><path d="M44 28 A16 16 0 1 1 38 15"/><path d="M38 6 V15 H47"/></svg>
      <div class="service-name">Ongoing<br>Optimization</div>
    </div>

    <div class="service">
      <svg class="service-icon" viewBox="0 0 56 56" fill="none" stroke="#333" stroke-width="3"><path d="M6 26 L16 16 L26 22 L36 16 L50 26"/><path d="M16 30 L24 38 M22 28 L30 36 M28 26 L36 34"/><path d="M6 26 L20 40 M50 26 L36 40"/></svg>
      <div class="service-name">Contract Negotiation<br>&amp; Relationship Management</div>
    </div>
    <div class="service">
      <svg class="service-icon" viewBox="0 0 56 56" fill="none" stroke="#333" stroke-width="3"><path d="M10 22 H20 L40 10 V46 L20 34 H10 Z"/><path d="M20 34 L24 46"/></svg>
      <div class="service-name">Direct Advertiser<br>Management</div>
    </div>
    <div class="service">
      <svg class="service-icon" viewBox="0 0 56 56" fill="none" stroke="#333" stroke-width="3"><path d="M28 6 L46 14 V28 C46 40 38 47 28 50 C18 47 10 40 10 28 V14 Z"/><path d="M19 28 L26 35 L38 22"/></svg>
      <div class="service-name">Quality<br>Control</div>
    </div>
    <div class="service">
      <svg class="service-icon" viewBox="0 0 56 56" fill="none" stroke="#333" stroke-width="3"><rect x="8" y="18" width="40" height="28"/><path d="M20 18 V12 H36 V18 M8 30 H48"/></svg>
      <div class="service-name">Business<br>Development</div>
    </div>
  </div>
</section>

<section class="welcome">
  <h2 class="section-title">Welcome To <em>Zornival</em></h2>
  <p class="welcome-text">We are an ad operations team working on behalf of publishers. Ad technology changes every month, and keeping up with it takes time, tools and plenty of manual work. We take that hassle off your desk: we set up your ad servers, configure networks and header bidding, track every tag and report on every dollar. Our goal is simple, to bring each client to the top of their revenue potential while they focus on creating great content for their readers.</p>
  <span class="btn">Read More</span>
</section>

<section class="tools">
  <h2 class="section-title"><em>Our</em> Tools &amp; Technologies<span class="title-rule"></span></h2>
  <div class="tool-list">
    <div class="tool">
      <div class="tool-icon"><svg width="52" height="52" viewBox="0 0 52 52" fill="none" stroke="#fff" stroke-width="3"><rect x="6" y="8" width="40" height="36"/><path d="M14 36 V28 M22 36 V20 M30 36 V24 M38 36 V16"/></svg></div>
      <div class="tool-body">
        <div class="tool-name">Reporting &amp;<br>Optimization</div>
        <p class="tool-desc">Clear daily reports across every network, with tuning done for you.</p>
      </div>
    </div>
    <div class="tool">
      <div class="tool-icon"><svg width="52" height="52" viewBox="0 0 52 52" fill="none" stroke="#fff" stroke-width="3"><rect x="6" y="10" width="40" height="30"/><path d="M18 46 H34 M26 40 V46 M14 20 H38 M14 28 H30"/></svg></div>
      <div class="tool-body">
        <div class="tool-name">Header Bidder<br>Configuration</div>
        <p class="tool-desc">More demand competing for each impression, set up and monitored.</p>
      </div>
    </div>
  </div>
</section>

<section class="partners">
  <div class="partner-row">
    <div class="partner-badge" role="img" aria-label="Partner badge"><span class="mark"></span></div>
    <div class="partner-badge" role="img" aria-label="Partner badge"><span class="mark"></span></div>
    <div class="partner-badge" role="img" aria-label="Certified partner badge"><span class="mark"></span></div>
  </div>
</section>

<section class="contact">
  <h2 class="contact-title">Ready to Maximize Your Monetization?</h2>
  <p class="contact-sub">Send us a few details about your site and we will be in touch within one day.</p>
  <form class="contact-form">
    <div class="field-row">
      <div class="field">Name</div>
      <div class="field">Website</div>
      <div class="field">Message</div>
    </div>
    <span class="btn">Submit</span>
  </form>
</section>

<footer class="site-footer">
  <span class="copy">Copyright © 2016 Zornival. All Rights Reserved.</span>
  <span class="mail">hello@zornival.com</span>
</footer>

</body>
</html>
```